We need a template newsletter design for our quarterly newsletter that we issue to employees. The newsletter generally holds updates from different departments such as:

CEO
Finance
Operations
Human Resources, ETC
(Please allow the pages to be copied)

I am looking for a template that has headings on each page, text space and image space. I am looking for a funky hip design with some great colour and creative imagination.

If you could create a cover page that includes the name "Harbourlinks" and the edition "Month, Year".

There is no requirements for specific logos or colours to be incorporated into this newsletter.

If possible I would like each page to have a different layout/design but for it to still flow as one newsletter. (Work with 4 pages/headings as listed above)

The document must be produced in InDesign.

Reason: Hi Guys, Whilst I love the designs submitted I am looking for a less formal and more creative funky design. Project is extended another 2 days. Thank you Merv

```html
<!DOCTYPE html>
<html lang="en">
<head>
<meta charset="utf-8">
<title>Harbourlinks Newsletter</title>
<link href="https://fonts.googleapis.com/css2?family=Montserrat:wght@300;400;500;700&display=swap" rel="stylesheet">
<style>
  :root {
    --brand-blue: #2eaae6;
    --ink: #3a3a3a;
    --body-grey: #5a5a5a;
    --white: #ffffff;
  }
  * { margin: 0; padding: 0; box-sizing: border-box; }
  html, body { width: 1014px; height: 1200px; overflow: hidden; background: var(--white); }
  body { font-family: "Montserrat", sans-serif; color: var(--ink); position: relative; }

  .top-band { position: absolute; left: 0; top: 0; width: 1014px; height: 10px; background: var(--brand-blue); }

  .masthead-title {
    position: absolute; left: 0; width: 1014px; top: 42px; text-align: center;
    font-size: 88px; font-weight: 700; letter-spacing: -2px; line-height: 1; color: var(--ink);
  }
  .edition-date {
    position: absolute; right: 155px; top: 118px;
    font-size: 22px; font-weight: 500; color: var(--ink); white-space: nowrap;
  }

  .feature-photo {
    position: absolute; left: 149px; top: 218px; width: 310px; height: 265px;
    background: linear-gradient(135deg, #8d8d8d 0%, #cfcfcf 45%, #6e6e6e 100%);
    overflow: hidden;
  }
  .feature-photo svg { position: absolute; right: 0; bottom: 0; }

  .feature-text {
    position: absolute; left: 507px; top: 220px; width: 442px;
    font-size: 21.8px; font-weight: 300; line-height: 32.4px; color: var(--body-grey);
  }

  .updates-heading {
    position: absolute; left: 0; width: 1020px; top: 538px; text-align: center;
    font-size: 21.5px; font-weight: 500; color: var(--ink); white-space: nowrap;
  }
  .department-list { position: absolute; left: 365px; top: 594px; list-style: none; }
  .department-list li {
    display: flex; align-items: center; height: 41px;
    font-size: 22px; font-weight: 500; color: var(--ink); white-space: nowrap;
  }
  .department-list svg { width: 25px; height: 25px; margin-right: 10px; }

  .teaser { position: absolute; top: 818px; width: 208px; }
  .teaser-photo {
    width: 196px; height: 151px; margin-left: 13px; overflow: hidden;
  }
  .teaser-photo span {
    display: block; width: 196px; height: 196px; border-radius: 50%;
  }
  .teaser-bar { width: 208px; height: 57px; background: var(--brand-blue); }
  .teaser-caption {
    margin-top: 9px; width: 260px; white-space: nowrap;
    font-size: 22px; font-weight: 500; line-height: 27px; color: var(--ink);
  }
  .teaser-1 { left: 79px; }
  .teaser-2 { left: 401px; }
  .teaser-3 { left: 715px; }
  .teaser-1 .teaser-photo span { background: linear-gradient(160deg, #d9dde2 0%, #3d3d3d 70%, #1f1f1f 100%); }
  .teaser-2 .teaser-photo span { background: linear-gradient(160deg, #b7cfd8 0%, #8a8f96 50%, #2b2b2b 100%); }
  .teaser-3 .teaser-photo span { background: linear-gradient(160deg, #c9b5a3 0%, #e5e2dd 50%, #b7a093 100%); }

  .site-footer {
    position: absolute; left: 0; top: 1130px; width: 1014px; height: 70px;
    background: var(--brand-blue); color: var(--white);
    display: flex; align-items: center; justify-content: center;
    font-size: 20px; font-weight: 500; white-space: nowrap;
  }
</style>
</head>
<body>
  <div class="top-band"></div>

  <h1 class="masthead-title">Harbourlinks</h1>
  <p class="edition-date">16 th augest ,2016</p>

  <div class="feature-photo" role="img" aria-label="Photo of smiling call centre staff wearing headsets">
    <svg width="100" height="95" viewBox="0 0 100 95" aria-hidden="true">
      <polygon points="100,0 100,95 0,95" fill="#2eaae6"/>
    </svg>
  </div>

  <p class="feature-text">Lorem ipsum dolor sit amet, consectetur adipisicing elit, sed do eiusmod tempor incididunt ut labore et dolore magna aliqua. Ut enim ad minim veniam, quis nostrud exercitation ullamco laboris nisi ut aliquip ex ea commodo consequat. Duis aute irure dolor in reprehenderit in voluptate velit esse cillum dolore eu</p>

  <h2 class="updates-heading">Watch Latest updates about this section here</h2>

  <ul class="department-list">
    <li><svg viewBox="0 0 24 24" aria-hidden="true"><path d="M20 10.5A8.5 8.5 0 1 1 15.5 4" fill="none" stroke="#3a3a3a" stroke-width="2.6" stroke-linecap="round"/><path d="M7.5 11.5l4 4L21 5" fill="none" stroke="#3a3a3a" stroke-width="2.8" stroke-linecap="round" stroke-linejoin="round"/></svg>CEO</li>
    <li><svg viewBox="0 0 24 24" aria-hidden="true"><path d="M20 10.5A8.5 8.5 0 1 1 15.5 4" fill="none" stroke="#3a3a3a" stroke-width="2.6" stroke-linecap="round"/><path d="M7.5 11.5l4 4L21 5" fill="none" stroke="#3a3a3a" stroke-width="2.8" stroke-linecap="round" stroke-linejoin="round"/></svg>Finance</li>
    <li><svg viewBox="0 0 24 24" aria-hidden="true"><path d="M20 10.5A8.5 8.5 0 1 1 15.5 4" fill="none" stroke="#3a3a3a" stroke-width="2.6" stroke-linecap="round"/><path d="M7.5 11.5l4 4L21 5" fill="none" stroke="#3a3a3a" stroke-width="2.8" stroke-linecap="round" stroke-linejoin="round"/></svg>Operations</li>
    <li><svg viewBox="0 0 24 24" aria-hidden="true"><path d="M20 10.5A8.5 8.5 0 1 1 15.5 4" fill="none" stroke="#3a3a3a" stroke-width="2.6" stroke-linecap="round"/><path d="M7.5 11.5l4 4L21 5" fill="none" stroke="#3a3a3a" stroke-width="2.8" stroke-linecap="round" stroke-linejoin="round"/></svg>Human Resources, ETC</li>
  </ul>

  <section class="teaser teaser-1">
    <div class="teaser-photo"><span role="img" aria-label="Photo of a busy businessman in a dark suit juggling phone and devices"></span></div>
    <div class="teaser-bar"></div>
    <p class="teaser-caption">What we do evoluve<br>and explore</p>
  </section>

  <section class="teaser teaser-2">
    <div class="teaser-photo"><span role="img" aria-label="Photo of two smiling colleagues in business attire"></span></div>
    <div class="teaser-bar"></div>
    <p class="teaser-caption">contract us what<br>to &nbsp;say hello</p>
  </section>

  <section class="teaser teaser-3">
    <div class="teaser-photo"><span role="img" aria-label="Photo of a doctor talking with a young child"></span></div>
    <div class="teaser-bar"></div>
    <p class="teaser-caption">Careers Thinking of<br>Joining us</p>
  </section>

  <footer class="site-footer">Copyright © 2016 Lumenway | Webmail | Login</footer>
</body>
</html>
```